Copperleaf Motorized Shade Business Card

Hello, we've had our logo made. Now we are looking for a clean and cool looking business card. One side can just be the logo with any design elements that might look good with it. The other side will be Name, Phone Number and Email. There will not be an address on the card.

```html
<!DOCTYPE html>
<html lang="en">
<head>
<meta charset="utf-8">
<title>Copperleaf Motorized Shade – Business Card</title>
<link rel="stylesheet" href="https://fonts.googleapis.com/css2?family=Montserrat:wght@400;600;700&display=swap">
<style>
  :root {
    --navy: #0a3b74;
    --navy-faint: #5b7da6;
    --sky: #1aa3e0;
    --sun: #f7c21c;
    --white: #ffffff;
    --paper: #f2f2f2;
  }
  * { margin: 0; padding: 0; box-sizing: border-box; }
  html, body {
    width: 1200px; height: 1200px; overflow: hidden;
    background: var(--paper);
    font-family: "Montserrat", sans-serif;
  }
  .sheet { position: relative; width: 1200px; height: 1200px; }

  .card {
    position: absolute; left: 150px;
    width: 900px; height: 514px;
    border-radius: 40px; overflow: hidden;
  }
  .card--front { top: 70px; background: var(--navy); }
  .card--back {
    top: 616px; background: var(--white);
    border: 12px solid var(--navy);
  }

  /* Brand name (stands where the logo sits) */
  .brand { position: absolute; display: flex; align-items: center; gap: 18px; }
  .brand__mark { width: 26px; height: 26px; background: var(--sun); }
  .brand__name { font-weight: 700; text-transform: uppercase; line-height: 1.05; }
  .brand__name span { display: block; }

  .card--front .brand { left: 90px; top: 200px; }
  .card--front .brand__name { color: var(--navy-faint); }
  .card--front .brand__line--main { font-size: 36px; letter-spacing: 1px; }
  .card--front .brand__line--sub { font-size: 15px; letter-spacing: 3px; }

  .card--back .brand { left: 50%; top: 50%; transform: translate(-50%, -50%); }
  .card--back .brand__name { color: var(--navy); }
  .card--back .brand__line--main { font-size: 72px; letter-spacing: 1px; }
  .card--back .brand__line--sub { font-size: 27px; letter-spacing: 7px; }
  .card--back .brand__mark { width: 40px; height: 40px; }

  /* Contact column */
  .contact-rail { position: absolute; left: 0; top: 0; width: 900px; height: 514px; }
  .person { position: absolute; left: 512px; top: 159px; }
  .person__name { color: var(--white); font-weight: 700; font-size: 24px; letter-spacing: 0.5px; text-transform: uppercase; line-height: 1.2; }
  .person__role { color: var(--sun); font-weight: 400; font-size: 15px; margin-top: 2px; }

  .contact-item {
    position: absolute; left: 512px;
    color: var(--white); font-size: 17px; letter-spacing: 0.5px; line-height: 1.35;
    transform: translateY(-50%);
  }
  .contact-item--phone { top: 257px; }
  .contact-item--email { top: 329px; }
</style>
</head>
<body>
<main class="sheet">

  <section class="card card--front" aria-label="Card front with contact details">
    <div class="brand">
      <div class="brand__name">
        <span class="brand__line--main">Copperleaf</span>
        <span class="brand__line--sub">Motorized Shade</span>
      </div>
    </div>

    <svg class="contact-rail" viewBox="0 0 900 514" aria-hidden="true">
      <polyline points="423,152 472,185 472,257 472,329 423,362" fill="none" stroke="var(--sun)" stroke-width="3"/>
      <g fill="var(--sun)">
        <circle cx="423" cy="152" r="6"/>
        <circle cx="423" cy="362" r="6"/>
        <circle cx="472" cy="185" r="19"/>
        <circle cx="472" cy="257" r="19"/>
        <circle cx="472" cy="329" r="19"/>
      </g>
      <g class="icon-person" fill="var(--navy)">
        <circle cx="472" cy="179" r="5"/>
        <path d="M462 194 q10 -14 20 0 z"/>
      </g>
      <path class="icon-phone" fill="var(--navy)" d="M464 249 l5 -2 3 7 -3 2 q2 5 7 8 l2 -3 7 3 -2 5 q-14 0 -19 -20 z"/>
      <g class="icon-mail">
        <rect x="462" y="322" width="20" height="14" fill="var(--navy)"/>
        <polyline points="462,322 472,331 482,322" fill="none" stroke="var(--sun)" stroke-width="2"/>
      </g>
    </svg>

    <div class="person">
      <p class="person__name">Dana Whitlock</p>
      <p class="person__role">Solution Manager</p>
    </div>
    <p class="contact-item contact-item--phone">+012 345 6789 / +012 345 6789</p>
    <p class="contact-item contact-item--email">urname@email.com</p>
  </section>

  <section class="card card--back" aria-label="Card back with brand name">
    <div class="brand">
      <div class="brand__mark"></div>
      <div class="brand__name">
        <span class="brand__line--main">Copperleaf</span>
        <span class="brand__line--sub">Motorized Shade</span>
      </div>
    </div>
  </section>

</main>
</body>
</html>
```